Drone company needs a brochure design

We would like a brochure design which compliments our existing logo, website and business card designs.

www.bramblecrest.com.au

```html
<!DOCTYPE html>
<html lang="en">
<head>
<meta charset="utf-8">
<title>Bramble Crest – Tri-fold Brochure</title>
<link href="https://fonts.googleapis.com/css2?family=Exo+2:wght@700;800&family=Montserrat:wght@400;600;700&display=swap" rel="stylesheet">
<style>
  :root {
    --blue: #1e9ad6;
    --blue-deep: #0f78b4;
    --ink: #231f20;
    --text: #2b2b2b;
    --paper: #ffffff;
    --stage: #d9dadc;
  }
  * { box-sizing: border-box; margin: 0; padding: 0; }
  html, body { width: 1200px; height: 773px; overflow: hidden; background: var(--stage); }
  body { font-family: "Montserrat", sans-serif; color: var(--text); }

  .brochure { display: flex; width: 1200px; height: 773px; }
  .panel { position: relative; width: 400px; height: 773px; background: var(--paper); overflow: hidden; }
  .panel + .panel { border-left: 1px solid #e2e3e5; }
  .panel-art { position: absolute; inset: 0; }
  .abs { position: absolute; }

  /* services panel */
  .photo-city { left: 0; top: 0; width: 400px; height: 232px;
    background: linear-gradient(180deg, #a9c7e3 0%, #d7e3ee 35%, #5b6f84 60%, #3f6b8a 100%); }
  .photo-harbour { left: 0; top: 618px; width: 400px; height: 155px;
    background: linear-gradient(180deg, #e6ebf0 0%, #8ea2b4 35%, #2c5d8c 70%, #1e4a74 100%); }

  .tab { position: absolute; left: 14px; background: var(--blue); color: #fff;
    font-family: "Exo 2", sans-serif; font-weight: 700; font-size: 20px; letter-spacing: .5px;
    padding: 5px 16px 6px 20px; }
  .tab-survey { top: 246px; }
  .tab-insurance { top: 428px; }
  .copy { position: absolute; left: 24px; width: 360px; font-size: 14px; line-height: 1.3; }
  .copy p + p { margin-top: 10px; }
  .copy-survey { top: 294px; }
  .copy-insurance { top: 476px; }

  /* about panel */
  .heading { font-family: "Exo 2", sans-serif; font-weight: 800; color: var(--blue-deep); font-size: 25px; letter-spacing: .5px; }
  .about { left: 32px; top: 200px; width: 340px; }
  .about p { margin-top: 6px; font-size: 14.5px; line-height: 1.35; text-align: justify; }
  .contact { left: 32px; top: 400px; width: 350px; }
  .contact .name { margin-top: 6px; font-weight: 700; font-size: 21px; color: var(--ink); }
  .contact .name small { font-size: 11px; }
  .contact dl { margin-top: 4px; font-size: 14px; line-height: 1.65; }
  .contact dt { display: inline; }
  .contact dd { display: inline; color: var(--blue); font-weight: 600; }
  .contact dd::after { content: "\A"; white-space: pre; }

  .wordmark { font-family: "Montserrat", sans-serif; font-weight: 700; color: var(--ink);
    display: flex; align-items: center; gap: 10px; white-space: nowrap; }
  .wordmark .dot { width: 14px; height: 14px; border-radius: 50%; background: var(--blue); }
  .wordmark-mid { left: 70px; top: 545px; font-size: 28px; }
  .wordmark-front { left: 80px; top: 62px; font-size: 32px; }

  /* cover panel */
  .photo-drone { left: 0; top: 170px; width: 400px; height: 330px;
    background: linear-gradient(180deg, #7fa2b4 0%, #a6c1cc 45%, #c7d9de 100%); }
  .photo-sunset { left: 0; top: 560px; width: 400px; height: 213px;
    background: linear-gradient(180deg, #c9d3dc 0%, #e8dcc8 35%, #8b7a66 65%, #3b3a36 100%); }
  .tagline { left: 0; top: 540px; width: 400px; text-align: center;
    font-family: "Exo 2", sans-serif; font-weight: 800; font-size: 27px; line-height: 1.12;
    color: var(--ink); text-transform: uppercase; letter-spacing: .5px; }
  .tagline .accent { color: var(--blue); font-size: 31px; }
  .url-band { left: 0; top: 706px; width: 400px; height: 67px; background: var(--blue-deep);
    color: #fff; font-weight: 600; font-size: 20px; letter-spacing: .5px;
    display: flex; align-items: center; justify-content: center; }
</style>
</head>
<body>
<main class="brochure">

  <section class="panel panel-services">
    <div class="abs photo-city" role="img" aria-label="Aerial photograph of a city skyline beside a river"></div>
    <h2 class="tab tab-survey">Survey &amp; Mapping</h2>
    <div class="copy copy-survey">
      <p>Reliable, timely survey data to enhance productivity or for precise Geo-location. Cost-effective alternative to conventional aerial surveys &amp; mapping.</p>
      <p>We are mobile and can travel to remote mine sights and rural farming operations.</p>
    </div>
    <h2 class="tab tab-insurance">Insurance &amp; Risk</h2>
    <div class="copy copy-insurance">
      <p>Bramble Crest are pleased to work with local insurance companies to inspect damage caused to land and properties. Assisting assessors and loss adjustors for claims.</p>
      <p>We also provide risk surveying support for underwriters.</p>
    </div>
    <div class="abs photo-harbour" role="img" aria-label="Aerial photograph of a harbour with a tugboat and port buildings"></div>
  </section>

  <section class="panel panel-about">
    <div class="abs photo-sunset" role="img" aria-label="Aerial photograph of a sunset over a lake and treeline"></div>
    <svg class="panel-art" width="400" height="773" viewBox="0 0 400 773" aria-hidden="true">
      <path d="M0 0 H400 V20 C300 40 160 60 0 200 Z" fill="var(--ink)"/>
      <path d="M0 200 C160 60 300 40 400 20 V46 C300 70 170 90 0 215 Z" fill="var(--blue)"/>
      <path d="M180 0 H250 C320 40 360 70 400 90 V110 C340 80 280 40 180 0 Z" fill="var(--blue)"/>
      <path d="M0 560 C150 620 290 600 400 500 V530 C290 620 150 640 0 600 Z" fill="var(--ink)"/>
      <path d="M0 600 C150 640 290 620 400 530 V0 H0 Z" fill="var(--paper)" clip-path="inset(215px 0 0 0)"/>
    </svg>
    <div class="abs about">
      <h2 class="heading">About Us</h2>
      <p>We provide premium aerial media solutions using the latest Unmanned Aerial Vehicles (UAV) technology. Offering a combination of stunning HD aerial filming and breathtaking aerial photography for a variety of different projects. The Bramble Crest team offer a unique service that is bespoke to your application and desired specification.</p>
    </div>
    <div class="abs contact">
      <h2 class="heading">Contact Details</h2>
      <p class="name">OWEN HARTLEY <small>(Director)</small></p>
      <dl>
        <dt>Phone: </dt><dd>040 555 0187</dd>
        <dt>Email: </dt><dd>contact@bramblecrest.com.au</dd>
        <dt>Address: </dt><dd>GERALDTON, WA 6530</dd>
      </dl>
    </div>
    <div class="abs wordmark wordmark-mid"><span class="dot"></span>Bramble Crest</div>
  </section>

  <section class="panel panel-cover">
    <div class="abs photo-drone" role="img" aria-label="Photograph of a white camera drone in flight against the sky"></div>
    <svg class="panel-art" width="400" height="773" viewBox="0 0 400 773" aria-hidden="true">
      <path d="M0 0 H400 V100 C300 150 150 170 0 150 Z" fill="var(--paper)"/>
      <path d="M0 150 C150 170 300 150 400 100 V122 C300 170 150 190 0 172 Z" fill="var(--blue)"/>
      <path d="M0 172 C150 190 300 170 400 122 V142 C300 190 150 205 0 190 Z" fill="var(--ink)"/>
      <path d="M0 500 C120 440 280 440 400 480 V773 H0 Z" fill="var(--blue)"/>
      <path d="M0 520 C120 462 280 462 400 500 V773 H0 Z" fill="var(--ink)"/>
      <path d="M0 534 C120 478 280 478 400 514 V773 H0 Z" fill="var(--paper)"/>
    </svg>
    <div class="abs wordmark wordmark-front"><span class="dot"></span>Bramble Crest</div>
    <p class="abs tagline">Let us<br>capture your<br>vision and provide<br>you with that<br><span class="accent">ultimate vantage</span></p>
    <div class="abs url-band">www.bramblecrest.com.au</div>
  </section>

</main>
</body>
</html>
```